Webdesign für Frauen-Personal-Training
Sehr schnelle Umsetzung meiner Wünsche und Ideen
Zielgruppe
Personal Training für Frauen in Führungspositionen ab 30 Jahren
Aufgabenstellung
Bilderwelt stimmig, Farbfokus auf CI Farben (im Anhang wie auch Logo), 1/3 Text, 2/3 Bilderwelt
- Hamburger Menü, kein klassisches
- Footer: Anschrift, Datenschutz, Impressum
- Headerimage mit Seitentitel im Bild, Titelunterschrift 2/3 der Bildschirmhöhe
- Berücksichtigung von Whitespace
- Verwendung von Icons zum Beispiel auf der Startseite beim Punkt 'du suchst - ich biete'
Seiten:
- Startseite: Einstieg für Besucher der Homepage in der Richtung 'du suchst, ich biete', abschließend Formular --> Abschluss Kontaktformular
- Training: Trainingsweise und Arbeitsweise beschreiben
- Über mich (Aufbau der Seite gleich wie 'Training' und 'Preise'): Professionelle Erfahrungen in Richtung training, Ernährung, Gesundheit --> Abschluss: CTA 'Nimm Kontakt zu mir auf und informiere dich in einem persönlichen Gespräch --> Link auf Kontaktseite
- Räumlichkeiten --> Abschluss: CTA 'Nimm Kontakt zu mir auf und informiere dich in einem persönlichen Gespräch --> Link auf Kontaktseite
- Preise --> Abschluss: CTA 'Nimm Kontakt zu mir auf und informiere dich in einem persönlichen Gespräch --> Link auf Kontaktseite
- Kontaktseite (Landing Page)
(- Impressum / Datenschutzseite)
Beispielseite:
https://www.quintello.com/rastavoni

```html
<!DOCTYPE html>
<html lang="de">
<head>
<meta charset="utf-8">
<title>Formwerkstatt – Personal Training für Frauen</title>
<link rel="stylesheet" href="https://fonts.googleapis.com/css2?family=Titillium+Web:wght@400;600&family=Rubik:wght@400;500&display=swap">
<style>
:root{
  --green:#5f9a72;
  --green-box:#689e79;
  --olive:#7b7459;
  --grey:#ececec;
  --ink:#2b2b2b;
  --muted:#555;
  --dark:#1f1f1f;
  --white:#fff;
}
*{margin:0;padding:0;box-sizing:border-box}
html,body{width:1200px;height:4658px;overflow:hidden}
body{position:relative;background:var(--white);font-family:"Rubik",sans-serif;color:var(--ink)}
.abs{position:absolute}
.heading{font-family:"Titillium Web",sans-serif;font-weight:400;color:var(--ink);letter-spacing:.5px}
.eyebrow{font-size:14px;color:var(--green);text-transform:uppercase;letter-spacing:.3px}
.rule{height:3px;width:62px;background:var(--green)}
.body-text{font-size:11.5px;line-height:22.5px;color:var(--muted)}
.btn{display:flex;align-items:center;justify-content:center;background:var(--green);color:var(--white);font-size:12px;font-weight:500;letter-spacing:1.5px;text-transform:uppercase}
.photo{background:linear-gradient(135deg,#c9d2dc,#7f93ab 55%,#2c3f66)}
.feature{width:170px}
.feature svg{width:36px;height:36px;stroke:var(--green);fill:none;stroke-width:1.4}
.feature h3{font-family:"Titillium Web",sans-serif;font-weight:400;font-size:18px;margin:14px 0 8px;color:var(--ink)}
.feature p{font-size:11px;line-height:22px;color:var(--muted)}
.callout{background:var(--green-box);color:var(--white);font-size:18.5px;line-height:30px;padding:30px 28px}
.course-label{background:var(--white);font-family:"Titillium Web",sans-serif;font-size:19px;line-height:21px;color:var(--ink)}
.arrow{height:1px;background:currentColor}
</style>
</head>
<body>

<!-- Header / Hero -->
<div class="abs" style="left:484px;top:0;width:716px;height:647px;background:var(--olive)"></div>
<div class="abs heading" style="left:94px;top:16px;font-size:24px;font-weight:600;color:var(--green)">Formwerkstatt</div>
<div class="abs" style="left:96px;top:46px;font-size:8px;color:var(--green)">Personal Training für Frauen</div>
<div class="abs" style="left:1076px;top:27px;width:28px">
  <div style="height:2px;background:#fff;margin-bottom:6px"></div>
  <div style="height:2px;background:#fff"></div>
</div>
<div class="abs photo" role="img" aria-label="Lächelnde Geschäftsfrau vor Bürogebäuden" style="left:94px;top:63px;width:1012px;height:530px;background:linear-gradient(100deg,#e6e8ea 0%,#c6ccd4 40%,#5f7598 70%,#223a6a 100%)"></div>
<div class="abs eyebrow" style="left:233px;top:240px">Unsere Strategie</div>
<div class="abs heading" style="left:231px;top:264px;font-size:40px;line-height:40px;color:#222">90% der Frauen in<br>Führungspositionen<br>bewegen sich zu wenig</div>
<div class="abs btn" style="left:235px;top:419px;width:166px;height:38px">Mehr Info</div>
<div class="abs" style="left:235px;top:620px;width:172px;height:4px;display:flex;align-items:center;color:#999">
  <div class="arrow" style="width:44px"></div>
  <div style="width:4px;height:4px;border-radius:50%;background:#333;margin-left:18px"></div>
  <div style="width:4px;height:4px;border-radius:50%;background:#bbb;margin-left:16px"></div>
  <div style="width:4px;height:4px;border-radius:50%;background:#bbb;margin-left:16px"></div>
  <div class="arrow" style="width:46px;margin-left:16px;background:#333"></div>
</div>

<!-- Sie suchen -->
<div class="abs" style="left:0;top:894px;width:716px;height:358px;background:var(--grey)"></div>
<div class="abs rule" style="left:233px;top:772px"></div>
<h2 class="abs heading" style="left:231px;top:790px;font-size:38px">Sie suchen</h2>
<p class="abs body-text" style="left:233px;top:873px;width:548px">Lorem ipsum dolor sit amet, consectetur adipiscing elit. Curabitur fermentum placerat augue ut volut­pat. Pellentesque ultrices finibus justo, non cursus ante lacinia sit amet. Donec porttitor ex odio, nec po­suere nibh convallis vel. Duis tempor orci sit amet aliquet blandit. Integer congue odio id felis ornare, non tempus velit sagittis. Proin ac enim neque. Morbi non sagittis leo, ut tincidunt enim. Phasellus non dolor sit amet orci dignissim mollis. Morbi ut dapibus ligula. Sed eget sagittis justo.</p>

<div class="abs feature" style="left:233px;top:1028px">
  <svg viewBox="0 0 36 36"><circle cx="16" cy="19" r="13"/><circle cx="16" cy="19" r="8"/><circle cx="16" cy="19" r="3"/><path d="M16 19 31 5M27 5h4v4"/></svg>
  <h3>Kompetenz</h3><p>Jemanden, der auf Ihre Anliegen, Wünsche und Fragen die richtigen Antworten kennt</p>
</div>
<div class="abs feature" style="left:421px;top:1028px">
  <svg viewBox="0 0 36 36"><circle cx="18" cy="18" r="16"/><circle cx="18" cy="18" r="12"/><path d="M18 10l2.4 5 5.4.6-4 3.7 1.1 5.3-4.9-2.7-4.9 2.7 1.1-5.3-4-3.7 5.4-.6z"/></svg>
  <h3>Individualität</h3><p>Jemanden, der ein auf Sie und Ihre Wünsche zugeschneidertes Konzept erarbeitet und durchführt</p>
</div>
<div class="abs feature" style="left:609px;top:1028px">
  <svg viewBox="0 0 36 36"><path d="M18 3 34 32H2z"/><path d="M18 7 30 29H6z"/><path d="M18 14v8M18 25v2"/></svg>
  <h3>Aufmerksamkeit</h3><p>Jemanden, der sich voll und ganz auf Sie konzentriert</p>
</div>
<div class="abs feature" style="left:795px;top:1028px">
  <svg viewBox="0 0 36 36"><rect x="7" y="15" width="22" height="19"/><path d="M11 15V9a7 7 0 0 1 14 0v6"/><circle cx="18" cy="23" r="2.5"/><path d="M18 25.5V29"/></svg>
  <h3>Diskretion</h3><p>Einen Ort, an dem Sie selbst sein können</p>
</div>

<!-- Über mich -->
<div class="abs eyebrow" style="left:233px;top:1376px">Über mich</div>
<h2 class="abs heading" style="left:231px;top:1398px;font-size:38px;line-height:40px">Meine persönliche<br>Geschichte</h2>
<p class="abs body-text" style="left:421px;top:1520px;width:550px">Suspendisse ut auctor massa. Nunc a semper odio. Pellentesque volutpat dolor sit amet gravida suscipit. Integer ultricies neque diam, sit amet rhoncus dui vehicula sit amet. Etiam a vestibulum turpis. Proin purus quam, egestas a massa convallis, pellentesque volutpat risus. Proin maximus ornare eros viverra viverra. Interdum et malesuada fames ac ante ipsum primis in faucibus. Vestibulum tristique neque sit amet lectus mattis, ut placerat eros porta. Proin purus quam, egestas a massa convallis, pellentesque volutpat risus.</p>
<div class="abs photo" role="img" aria-label="Geschäftsfrau beim Händedruck vor Bürotürmen" style="left:419px;top:1704px;width:546px;height:311px;background:linear-gradient(110deg,#3f4b66 0%,#aab4c2 45%,#d8dde4 60%,#2f4b7e 100%)"></div>
<div class="abs callout" style="left:233px;top:1854px;width:295px;height:211px">Mit unseren Spezialisten und Experten, die Ihnen zur Verfügung stehen, werden Sie komplexe Probleme mit Zuversicht angehen</div>

<!-- Ich biete -->
<div class="abs eyebrow" style="left:233px;top:2186px">Beratungsleistungen</div>
<h2 class="abs heading" style="left:231px;top:2200px;font-size:38px">Ich bitte</h2>
<p class="abs body-text" style="left:233px;top:2275px;width:548px">Lorem ipsum dolor sit amet, consectetur adipiscing elit. Curabitur fermentum placerat augue ut volut­pat. Pellentesque ultrices finibus justo, non cursus ante lacinia sit amet. Donec porttitor ex odio, nec po­suere nibh convallis vel. Duis tempor orci sit amet aliquet blandit. Integer congue odio id felis ornare, non tempus velit sagittis. Proin ac enim neque. Morbi non sagittis leo, ut tincidunt enim. Phasellus non dolor sit amet orci dignissim mollis. Morbi ut dapibus ligula. Sed eget sagittis justo.</p>
<div class="abs" style="left:484px;top:2396px;width:716px;height:358px;background:var(--grey)"></div>

<div class="abs feature" style="left:233px;top:2438px">
  <svg viewBox="0 0 36 36"><circle cx="16" cy="19" r="13"/><circle cx="16" cy="19" r="8"/><circle cx="16" cy="19" r="3"/><path d="M16 19 31 5M27 5h4v4"/></svg>
  <h3>Kompetenz</h3><p>Zahlreiche Aus- und Fortbildungen, langjährige Praxis und der Anspruch, jeden Tag besser zu werden</p>
</div>
<div class="abs feature" style="left:421px;top:2438px">
  <svg viewBox="0 0 36 36"><circle cx="18" cy="18" r="16"/><circle cx="18" cy="18" r="12"/><path d="M18 10l2.4 5 5.4.6-4 3.7 1.1 5.3-4.9-2.7-4.9 2.7 1.1-5.3-4-3.7 5.4-.6z"/></svg>
  <h3>Individualität</h3><p>"es kommt darauf an", nach diesem Motto schauen wir gemeinsam, was für Sie passt und was nicht</p>
</div>
<div class="abs feature" style="left:609px;top:2438px">
  <svg viewBox="0 0 36 36"><path d="M18 3 34 32H2z"/><path d="M18 7 30 29H6z"/><path d="M18 14v8M18 25v2"/></svg>
  <h3>Aufmerksamkeit</h3><p>Im Training stehst du im Mittelpunkt</p>
</div>
<div class="abs feature" style="left:795px;top:2438px">
  <svg viewBox="0 0 36 36"><rect x="7" y="15" width="22" height="19"/><path d="M11 15V9a7 7 0 0 1 14 0v6"/><circle cx="18" cy="23" r="2.5"/><path d="M18 25.5V29"/></svg>
  <h3>Diskretion</h3><p>Meine Akzeptanz in Kombination mit eigenen Räumlichkeiten</p>
</div>
<div class="abs btn" style="left:506px;top:2653px;width:188px;height:38px">Kontakt zu mir</div>

<!-- Kurse -->
<div class="abs rule" style="left:233px;top:2877px"></div>
<h2 class="abs heading" style="left:231px;top:2890px;font-size:38px">Unsere Kurse</h2>
<div class="abs photo" role="img" aria-label="Team legt die Hände übereinander" style="left:233px;top:2978px;width:358px;height:253px;background:linear-gradient(135deg,#e8d8cc,#b8a8a0 40%,#d9c24a 75%,#8892a6)"></div>
<div class="abs" style="left:276px;top:3180px;width:315px;height:105px;background:var(--olive)"></div>
<div class="abs course-label" style="left:296px;top:3180px;width:309px;height:87px;padding:20px 22px">Teambuilding und<br>Teammanagement<br>Online Kurse</div>
<div class="abs arrow" style="left:541px;top:3214px;width:48px;color:var(--green)"></div>
<div class="abs photo" role="img" aria-label="Hände mit Tablet und Diagrammen auf dem Schreibtisch" style="left:609px;top:3079px;width:356px;height:201px;background:linear-gradient(135deg,#c4ccd6,#eef0f2 45%,#8ea0b8 80%,#5d6f8a)"></div>
<div class="abs" style="left:609px;top:3280px;width:63px;height:52px;background:linear-gradient(#aab4c0,#6e7c90)"></div>
<div class="abs course-label" style="left:672px;top:3280px;width:293px;height:72px;padding:20px 22px">Betriebsführung und<br>strategische Planung</div>
<div class="abs arrow" style="left:917px;top:3323px;width:46px;color:#555"></div>
<p class="abs body-text" style="left:421px;top:3393px;width:545px">Nam a pharetra lacus. Maecenas a sapien interdum felis vehicula egestas. Sed dapibus sapien sed eros pretium dignissim. Curabitur consequat dui vel pellentesque commodo. Proin quis turpis finibus, congue nibh sit amet, molestie tellus. Orci varius natoque penatibus et magnis dis parturient montes, nascetur ridiculus mus. Nam nibh diam, mattis et pellentesque eget, commodo at tortor.</p>
<div class="abs btn" style="left:423px;top:3531px;width:168px;height:40px">Mehr Info</div>

<!-- Person / CTA -->
<div class="abs photo" role="img" aria-label="Porträt der Trainerin mit verschränkten Armen" style="left:233px;top:3695px;width:483px;height:338px;background:linear-gradient(90deg,#f2f2f2 0%,#e6e3df 35%,#2e4a7a 55%,#eeeeee 80%,#f6f6f6 100%)"></div>
<div class="abs" style="left:734px;top:3744px;font-size:11px;line-height:20px;color:var(--muted)">Mara Lindqvist<br>Gründer</div>
<div class="abs" style="left:734px;top:3810px;font-size:11px;color:var(--muted)">Berlin 2019</div>
<div class="abs" style="left:952px;top:3811px;width:11px;height:11px;background:#222"></div>
<div class="abs callout" style="left:672px;top:3872px;width:293px;height:212px;padding:30px 28px">Nimm Kontakt zu mir auf und informiere dich in einem persönlichen Gespräch</div>
<div class="abs arrow" style="left:890px;top:4040px;width:46px;color:#fff"></div>

<!-- Kontaktformular -->
<div class="abs" style="left:0;top:4207px;width:840px;height:383px;background:var(--olive)"></div>
<div class="abs" style="left:94px;top:4270px;width:1012px;height:320px;background:var(--grey)"></div>
<div class="abs rule" style="left:569px;top:4331px"></div>
<h2 class="abs heading" style="left:0;width:1200px;top:4344px;text-align:center;font-size:40px">Kontaktformular</h2>
<div class="abs" style="left:0;width:1200px;top:4405px;text-align:center;font-size:17px;color:var(--ink)">Professionelle Erfahrungen in Richtung training, Ernährung, Gesundheit</div>
<div class="abs" style="left:421px;top:4456px;font-size:10px;font-weight:500;letter-spacing:1px">E-MAIL:</div>
<div class="abs" style="left:421px;top:4474px;width:356px;height:36px;background:#fff"></div>
<div class="abs arrow" style="left:712px;top:4491px;width:46px;color:#333"></div>
<div class="abs" style="left:421px;top:4510px;width:356px;height:3px;background:#d6d6d6"></div>
<div class="abs" style="left:421px;top:4510px;width:87px;height:3px;background:var(--green)"></div>
<div class="abs" style="left:758px;top:4522px;font-size:10px;font-weight:500">2/4</div>

<!-- Footer -->
<footer class="abs" style="left:0;top:4590px;width:1200px;height:68px;background:var(--dark);color:#fff;font-size:9px;font-weight:500;letter-spacing:1px">
  <span class="abs" style="left:233px;top:28px">IMPRESSUM</span>
  <span class="abs" style="left:322px;top:28px">DATENSCHUTZSEITE</span>
  <span class="abs" style="left:868px;top:28px;letter-spacing:0">© Formwerkstatt 2019</span>
</footer>

</body>
</html>
```